Business Card Design

We are a new residential construction company.our team is made up of young highly skilled tradesman of the next generation of carpenters coming through with new skills and ideas.we chose the name meridian as it means strikingly different from the rest as this is what we plan to be and we would like to portray this in our business card.we like Bold lettering as we want to make a statement, also the use of colour would be great as we want to stand out from the usual plain construction cards and logos.
I have attached a logo sketch I did as a rough idea if you can tidy it up or improve on it would be good.
I have also attached the LBP logo please include this on the card small but still legible.
open to any colourschemes ideas.
thanks
(note)please delete the LBP#804317 off from the card details please.
Industry/Entity Type
Construction
Contact Information for Business Card
MERIDIAN CONSTRUCTION LIMITED
Director:Tom Halvick
Mobile :0217364820
Email:Meridian.Construction@quillpost.example
Address:48 Wendle place,Ashgrove park 2091,Auckland
LBP#BP804317

```html
<!DOCTYPE html>
<html lang="en">
<head>
<meta charset="utf-8">
<title>Meridian Construction – Business Card</title>
<link rel="stylesheet" href="https://fonts.googleapis.com/css2?family=Tinos:wght@400;700&family=Archivo+Black&display=swap">
<style>
  :root {
    --page-bg: #d9d9d9;
    --card-top: #1fa8e4;
    --card-mid: #5cc3ee;
    --card-low: #8fd5f2;
    --title-ink: #1d5f78;
    --subtitle-ink: rgba(29, 95, 120, 0.55);
    --body-ink: #111111;
    --mark-ink: #1a1a1a;
    --glow-tone: rgba(30, 110, 150, 0.14);
  }
  * { box-sizing: border-box; margin: 0; padding: 0; }
  html, body {
    width: 1200px; height: 1200px; overflow: hidden;
    background: var(--page-bg);
  }
  body { display: flex; align-items: center; justify-content: center; }

  .business-card {
    position: relative;
    width: 1000px; height: 572px;
    background: linear-gradient(172deg, var(--card-top) 0%, var(--card-mid) 45%, var(--card-low) 100%);
    overflow: hidden;
    box-shadow: 0 6px 18px rgba(0,0,0,0.18);
  }
  .background-art {
    position: absolute; right: 40px; top: 110px;
    width: 360px; height: 400px;
    border-radius: 50%;
    background: radial-gradient(ellipse at center, var(--glow-tone) 0%, rgba(30,110,150,0) 70%);
  }
  .wordmark {
    position: absolute; left: 48px; top: 20px;
    font-family: "Tinos", "Times New Roman", serif;
    line-height: 1;
  }
  .wordmark__name {
    font-size: 112px; font-weight: 400; letter-spacing: 2px;
    color: var(--title-ink);
  }
  .wordmark__trade {
    margin-top: -4px;
    font-size: 74px; font-weight: 400; letter-spacing: 1px;
    color: var(--subtitle-ink);
  }
  .brand-mark {
    position: absolute; right: 78px; top: 190px;
    display: flex; align-items: center; gap: 10px;
    font-family: "Archivo Black", "Arial Black", sans-serif;
    font-size: 26px; color: var(--mark-ink);
  }
  .brand-mark__dot {
    width: 22px; height: 22px; border-radius: 50%;
    background: var(--mark-ink);
  }
  .contact-list {
    position: absolute; left: 40px; top: 322px;
    list-style: none;
    font-family: "Archivo Black", "Arial Black", sans-serif;
    font-size: 19px; color: var(--body-ink);
  }
  .contact-list li {
    display: flex; align-items: center; gap: 16px;
    height: 36px;
  }
  .contact-list svg { width: 20px; height: 24px; flex: none; }
  .address-block {
    position: absolute; right: 60px; bottom: 58px;
    font-family: "Archivo Black", "Arial Black", sans-serif;
    font-style: normal;
    font-size: 20px; line-height: 1.2; color: var(--body-ink);
    text-align: right;
  }
  .address-block__label { text-align: center; }
</style>
</head>
<body>
  <article class="business-card">
    <div class="background-art" role="img" aria-label="Faint tool illustration in the background"></div>

    <header class="wordmark">
      <h1 class="wordmark__name">MERIDIAN</h1>
      <p class="wordmark__trade">CONSTRUCTION</p>
    </header>

    <div class="brand-mark">
      <span class="brand-mark__dot"></span>
      <span class="brand-mark__name">MERIDIAN</span>
    </div>

    <ul class="contact-list">
      <li>
        <svg viewBox="0 0 20 24" aria-hidden="true"><circle cx="10" cy="6" r="5" fill="#333"/><rect x="4" y="12" width="12" height="12" rx="3" fill="#333"/></svg>
        <span>Tom Halvick</span>
      </li>
      <li>
        <svg viewBox="0 0 20 24" aria-hidden="true"><rect x="4" y="1" width="12" height="22" rx="2" fill="none" stroke="#333" stroke-width="2"/><rect x="7" y="4" width="6" height="7" fill="#333"/></svg>
        <span>0217364820</span>
      </li>
      <li>
        <svg viewBox="0 0 20 24" aria-hidden="true"><rect x="1" y="6" width="18" height="12" fill="#333"/><path d="M1 6 L10 13 L19 6" fill="none" stroke="#fff" stroke-width="1.5"/></svg>
        <span>meridian.construction@quillpost.example</span>
      </li>
    </ul>

    <address class="address-block">
      <div class="address-block__label">ADDRESS</div>
      <div>48 Wendle place, Ashgrove park</div>
      <div>2091, Auckland</div>
    </address>
  </article>
</body>
</html>
```